THE LARKWELL GROUP (Legal) Wordpress Design with Coding for Online Company

I need a Wordpress design with coding, pictures, content to be provided by me, fully responsive, and development. This is for a 6-7 page design.

Pages Needed: Home/About/THE LARKWELL GROUP/Process/FAQ/Contact Us/Blog.

The home page should be organized as followed:
-Steps in THE LARKWELL GROUP: Gather; Implement; Close (each step will come with content)
-Flat-Fee Price & Savings: Content will go here with a button to contact us (phone number) or just the phone number.
-You Have Questions, We Have Answers: five questions with content. Only one question answer to show at a time when clicked on the question from the list.
-Get to Know Us: a brief description with content about what we do and who we are.

Main image slogan: Helping Californians deal with loss with DIGNITY & UNDERSTATING (you may use a better slogan if you wish).

The Contact page should not have a map since we are an online company. We service the entire state of California in every county and city.

The About page should be simple, direct, and easy on the eye. It should have a brief description of who we are and it should have no more than 6 reasons why the client should hire us.

About our online California company. We are not attorneys but legal document assistants who prepare legal documents for probate estate when someone dies with or without a will and assets need to be distributed. We have a flat-fee for Formal THE LARKWELL GROUP of $999 and $699 for Informal THE LARKWELL GROUP. We are an online company and offer our services to the entire state of California in every county. We do everything over the phone and email. The turn around time for us to prepare the initial legal paperwork for the client is within 3-5 business days. We can prepare, file, serve and manage a probate matter from petition to closing. We are not attorneys so our prices are very affordable compare to the attorney.

The company name for the website will be www.thelarkwellgroup.com, The Larkwell Group.

I do not have a logo yet. The colors of the website should be easy on the eye and calming. THE SITE SHOULD BE SIMPLE AND STRAIGHT TO THE POINT. EASY TO NAVIGATE.

The company phone number should be very visible and should stand out to the client. It should also be clickable and ready to dial for smartphone users.

I do not want a contact form on the homepage. THE MAIN THING IS FOR THE POTENTIAL CLIENT TO CALL OUR OFFICE TO SIGN UP.

I do like some images of family or people since we are dealing with people who just lost a loved one. Not all the images have to be of people.

The site should not look like we practice law or that people can mistake us for attorneys.

Target Market(s)

People who just lost a loved one who had property, assets, in California but died with or without a will or trust. This is for people looking to hire non-attorneys.

Coding

Font styles to use
Serif

Colors

Designer to choose colors to be used in the design.

Requirements
Must have
• Refer to Project Description.
Nice to have
• The sample images provided is what I am attracted to for the homepage image.
Should not have

```html
<!DOCTYPE html>
<html lang="en">
<head>
<meta charset="utf-8">
<title>The Larkwell Group – Probate</title>
<link rel="stylesheet" href="https://fonts.googleapis.com/css2?family=Noto+Serif:ital,wght@0,400;0,700;1,400&display=swap">
<style>
:root{
  --brand:#0a5595;
  --brand-dark:#08477d;
  --green:#2f7d12;
  --ink:#333a40;
  --muted:#666d73;
  --light:#f1f1f1;
  --line:#dcdcdc;
  --white:#ffffff;
}
*{box-sizing:border-box;margin:0;padding:0}
html,body{width:1200px;height:2980px;overflow:hidden}
body{font-family:"Noto Serif",Georgia,serif;color:var(--ink);background:var(--white);position:relative}
.abs{position:absolute}
.btn{position:absolute;display:flex;align-items:center;justify-content:center;gap:8px;background:var(--brand);color:var(--white);font-weight:700;font-size:13px;border-radius:20px;text-transform:uppercase;white-space:nowrap}

/* header */
.site-header{left:0;top:0;width:1200px;height:104px;background:var(--brand)}
.brand-name{left:98px;top:28px;color:var(--white);font-weight:700;font-size:26px;letter-spacing:.5px}
.call-pill{left:936px;top:20px;width:162px;height:40px;border:1.5px solid var(--white);border-radius:20px;display:flex;align-items:center;gap:10px;padding-left:18px;color:var(--white);font-size:11px;font-weight:700;line-height:1.2}
.main-nav{left:0;top:74px;width:1102px;display:flex;justify-content:flex-end}
.main-nav a{color:var(--white);font-size:12px;font-weight:700;text-decoration:none;margin-left:40px}

/* hero */
.hero{left:0;top:104px;width:1200px;height:514px;background:linear-gradient(115deg,#3a1f1a 0%,#7a3a34 35%,#8a5a4a 60%,#b79a86 85%,#cdb9a8 100%)}
.hero-kicker{left:0;top:278px;width:1200px;text-align:center;color:var(--white);font-size:26px}
.hero-title{left:0;top:322px;width:1200px;text-align:center;color:var(--white);font-size:44px;font-weight:700;letter-spacing:1px}

/* steps */
.section-title{font-weight:700;font-size:30px;color:var(--ink);text-transform:uppercase}
.step{width:320px}
.step h3{font-size:16px;font-weight:700;margin-bottom:10px}
.step p{font-size:12px;line-height:22px;color:var(--muted)}

/* flat fee */
.fee-band{left:0;top:910px;width:1200px;height:326px;background:linear-gradient(180deg,#5c6f80 0%,#4f6a84 45%,#2f4f6d 100%)}
.fee-title{left:0;top:954px;width:1200px;text-align:center;color:var(--white);font-size:28px;font-weight:700}
.fee-copy{left:220px;top:1012px;width:760px;text-align:center;color:var(--white);font-size:12.5px;line-height:22px}

/* faq */
.faq{left:98px;top:1365px;width:1003px;border:1px solid var(--line)}
.faq-open-q{height:58px;background:var(--white);display:flex;align-items:center;padding-left:24px;font-size:13.5px;font-weight:700;border-bottom:1px solid var(--line)}
.faq-open-a{height:97px;background:#f7f7f7;padding:18px 0 0 24px;font-size:13px;color:var(--muted)}
.faq-open-a li{list-style:none;display:flex;align-items:center;gap:14px;margin-bottom:16px}
.faq-open-a li::before{content:"";width:10px;height:10px;border-radius:50%;background:var(--brand)}
.faq-q{height:52px;background:var(--brand);color:var(--white);display:flex;align-items:center;gap:14px;padding-left:24px;font-size:13.5px;font-weight:700;border-top:1px solid #3d7ab0}
.faq-q::before{content:"";border-left:6px solid var(--white);border-top:4px solid transparent;border-bottom:4px solid transparent}
.scrollbar{right:0;top:0;width:16px;height:155px;background:#e4e4e4}
.scrollbar::after{content:"";position:absolute;left:3px;top:16px;width:10px;height:120px;background:#c9c9c9}

/* know us */
.know-bg{left:0;top:1788px;width:1200px;height:478px;background:linear-gradient(90deg,#4a4f55 0%,#6b6e73 40%,#8a6d62 65%,#b8462e 100%)}
.know-title{left:0;top:1834px;width:1200px;text-align:center;color:var(--white);font-size:30px;font-weight:700}
.card{top:1918px;width:456px;height:274px;background:var(--white);text-align:center;padding-top:26px}
.card h3{font-size:21px;font-weight:700;text-transform:uppercase;line-height:30px}
.card .icon{display:block;width:38px;height:38px;margin:10px auto 10px;border-radius:6px}
.card p{font-size:12px;line-height:21px;color:var(--muted);width:380px;margin:0 auto}
.card .btn{top:210px}

/* testimonial */
.testi-title{left:0;top:2314px;width:1200px;text-align:center}
.avatar{left:546px;top:2374px;width:108px;height:108px;border-radius:50%;border:4px solid #e8e8e8;background:linear-gradient(180deg,#8aa0ad,#5e6e78)}
.quote{left:250px;top:2506px;width:700px;text-align:center;font-style:italic;font-size:12.5px;line-height:26px;color:var(--muted)}
.author{left:706px;top:2598px;font-size:13px;color:var(--ink)}

/* footer */
.footer-nav{left:0;top:2672px;width:1200px;height:66px;background:var(--light);border-top:1px solid #e2e2e2;border-bottom:1px solid #e2e2e2}
.footer-nav a{position:absolute;top:24px;transform:translateX(-50%);font-size:13px;color:var(--muted);text-decoration:none}
.newsletter{left:0;top:2766px;width:1200px;text-align:center;font-size:17px;font-weight:700;color:var(--ink)}
.signup{left:346px;top:2816px;width:500px;height:46px;border:1px solid var(--line);border-radius:23px;background:var(--white)}
.signup span{position:absolute;left:24px;top:14px;font-size:13px;color:var(--muted)}
.signup b{position:absolute;right:-1px;top:-1px;width:140px;height:46px;border-radius:23px;background:var(--brand);color:var(--white);font-size:13px;display:flex;align-items:center;justify-content:center}
.socials{left:0;top:2898px;width:1200px;display:flex;justify-content:center;gap:18px}
.socials i{width:16px;height:16px;border-radius:50%;display:block}
.copyright{left:0;top:2930px;width:1200px;text-align:center;font-size:11.5px;color:var(--muted)}
</style>
</head>
<body>

<header class="abs site-header">
  <div class="abs brand-name">THE LARKWELL GROUP</div>
  <a class="abs call-pill">
    <svg width="18" height="18" viewBox="0 0 24 24"><path fill="#fff" d="M6.6 10.8a15 15 0 0 0 6.6 6.6l2.2-2.2a1 1 0 0 1 1-.25 11.4 11.4 0 0 0 3.6.57 1 1 0 0 1 1 1V20a1 1 0 0 1-1 1A17 17 0 0 1 3 4a1 1 0 0 1 1-1h3.5a1 1 0 0 1 1 1c0 1.25.2 2.45.57 3.570a1 1 0 0 1-.25 1z"/></svg>
    <span>CALL US NOW<br>1-999-555-0142</span>
  </a>
  <nav class="abs main-nav">
    <a>HOME</a><a>ABOUT</a><a>PROBATE</a><a>PROCESS</a><a>FAQ</a><a>CONTACT US</a><a>BLOG</a>
  </nav>
</header>

<section class="abs hero" role="img" aria-label="Photo of a last will and testament with a pocket watch, keys and a pen"></section>
<div class="abs hero-kicker">Helping Californians deal with loss with</div>
<h1 class="abs hero-title">DIGNITY &amp; UNDERSTATING</h1>
<a class="btn" style="left:530px;top:405px;width:140px;height:36px;font-size:12px">Read More &gt;&gt;</a>

<h2 class="abs section-title" style="left:100px;top:674px">Steps in Probate</h2>
<div class="abs step" style="left:100px;top:734px"><h3>1. GATHER</h3><p>Lorem ipsum dolor sit amet, consectetur adipiscing elit, sed do eiusmod tempor incididunt ut labore et dolore magna aliqua. Ut enim ad minim veniam, quis nostrud exercitation ullamco laboris nisi ut aliquip.,</p></div>
<div class="abs step" style="left:443px;top:734px"><h3>2. IMPLEMENT</h3><p>Lorem ipsum dolor sit amet, consectetur adipiscing elit, sed do eiusmod tempor incididunt ut labore et dolore magna aliqua. Ut enim ad minim veniam, quis nostrud exercitation ullamco laboris nisi ut aliquip.,</p></div>
<div class="abs step" style="left:785px;top:734px"><h3>3. CLOSE</h3><p>Lorem ipsum dolor sit amet, consectetur adipiscing elit, sed do eiusmod tempor incididunt ut labore et dolore magna aliqua. Ut enim ad minim veniam, quis nostrud exercitation ullamco laboris nisi ut aliquip.,</p></div>

<section class="abs fee-band" role="img" aria-label="Photo of a family walking together on a beach at sunset"></section>
<h2 class="abs fee-title">FLAT-FEE PRICE &amp; SAVINGS</h2>
<p class="abs fee-copy">ed ut perspiciatis unde omnis iste natus error sit voluptatem accusantium doloremque laudantium, totam rem aperiam, eaque ipsa quae ab illo inventore veritatis et quasi architecto beatae vitae dicta sunt explicabo. Nemo enim ipsam voluptatem quia voluptas sit aspernatur aut odit aut fugit,sed quia consequuntur magni dolores eos qui ratione voluptatem sequi nesciunt.<br>Neque porro quisquam est, qui dolorem ipsum quia dolor</p>
<a class="btn" style="left:520px;top:1146px;width:160px;height:38px">Contact Us Now</a>

<h2 class="abs section-title" style="left:98px;top:1290px">FAQ</h2>
<div class="abs faq">
  <div class="faq-open-q"><svg width="20" height="10" viewBox="0 0 10 6"><path d="M1 1h7L4.5 5z" fill="#333a40"/></svg>Praesent eu ex eget metus porttitor tincidunt sed ut lacus. Mauris at purus nec elit sagittis auctor?</div>
  <ul class="faq-open-a">
    <li>Sed id massa sollicitudin, auctor eros eu, molestie enim. Nunc sem nunc, ullamcorper id cursus</li>
    <li>Finibus Bonorum et Malorum" by Cicero are also reproduced in their exact original form,</li>
  </ul>
  <div class="faq-q">Contrary to popular belief, Lorem Ipsum is not simply random text ?</div>
  <div class="faq-q">Lorem Ipsum has been the industry's standard dummy text ever since the 1500s ?</div>
  <div class="faq-q">Lorem Ipsum is that it has a more-or-less normal distribution of letters, as opposed to using 'Content here, content here' ?</div>
  <div class="faq-q">Finibus Bonorum et Malorum" by Cicero are also reproduced in their exact original form ?</div>
  <div class="abs scrollbar"></div>
</div>

<section class="abs know-bg" role="img" aria-label="Photo of a smiling woman in a red jacket working at a desk"></section>
<h2 class="abs know-title">GET TO KNOW US</h2>
<div class="abs card" style="left:116px">
  <h3>Who We Are</h3>
  <span class="icon" role="img" aria-label="Illustration of a small group of people" style="background:linear-gradient(135deg,#e07a6a,#5b8fc4)"></span>
  <p>Lorem ipsum dolor sit amet, consectetur adipiscing elit, sed do eiusmod tempor incididunt ut labore et dolore magna aliqua. Ut enim ad minim veniam, quis nostrud exercitation.</p>
  <a class="btn" style="left:156px;width:144px;height:36px">Learn More <svg width="14" height="10" viewBox="0 0 14 10"><path d="M0 5h11M8 1l4 4-4 4" stroke="#fff" stroke-width="2" fill="none"/></svg></a>
</div>
<div class="abs card" style="left:628px">
  <h3>What We Do</h3>
  <span class="icon" role="img" aria-label="Illustration of two gears" style="background:linear-gradient(135deg,#2a9bb8,#d8c21e)"></span>
  <p>Sed ut perspiciatis unde omnis iste natus error sit voluptatem accusantium doloremque laudantium, totam rem aperiam, eaque ipsa quae ab illo inventore veritatis ets.</p>
  <a class="btn" style="left:156px;width:144px;height:36px;background:var(--green)">Learn More <svg width="14" height="10" viewBox="0 0 14 10"><path d="M0 5h11M8 1l4 4-4 4" stroke="#fff" stroke-width="2" fill="none"/></svg></a>
</div>

<h2 class="abs section-title testi-title">Testimonial</h2>
<div class="abs avatar" role="img" aria-label="Portrait photo of the client giving the testimonial"></div>
<p class="abs quote">"Sed ut perspiciatis unde omnis iste natus error sit voluptatem accusantium doloremque laudantium, totam rem aperiam, eaque ipsa quae ab illo inventore veritatis et quasi architecto beatae vitae dicta sunt explicabo. Nemo enim ipsam voluptatem quia voluptas sit aspernatur aut odit aut fugit"</p>
<div class="abs author">- AUTHOR NAME</div>

<nav class="abs footer-nav">
  <a style="left:217px">Home</a><a style="left:338px">About</a><a style="left:463px">Probate</a><a style="left:592px">Process</a><a style="left:711px">FAQ</a><a style="left:841px">Contact Us</a><a style="left:970px">Blog</a>
</nav>
<h2 class="abs newsletter">SIGNUP FOR OUR NEWSLETTER</h2>
<div class="abs signup"><span>Email Address</span><b>SUBSCRIBE NOW</b></div>
<div class="abs socials">
  <i style="background:#2aa3e0"></i><i style="background:#3b5a9a"></i><i style="background:#1a74b0"></i><i style="background:#c9252c"></i>
</div>
<div class="abs copyright">Copyrights © 2017 The Larkwell Group . Allrights Reserved.</div>

</body>
</html>
```